Corvane Medical new year card

Hi,
I would like a New Year greetings card to send to my customers.

If you need to look at our logo : www.corvanemedical.com

If you want to play with images of our device, see
trelvacare.ca

The goal is to have a card to wish a happy new year and we look forward collaborating with them in the new year.

```html
<!DOCTYPE html>
<html lang="en">
<head>
<meta charset="utf-8">
<title>Corvane Medical – New Year Card</title>
<link href="https://fonts.googleapis.com/css2?family=Anton&family=Roboto:wght@500;700&family=Yellowtail&display=swap" rel="stylesheet">
<style>
  :root {
    --stage: #f1ece8;
    --card: #ffffff;
    --doodle: #f6ece3;
    --brand-grey: #6d6e71;
    --brand-orange: #ee7623;
    --year-red: #bb3a27;
    --script-red: #d63a2a;
    --script-tan: #c58a55;
    --device-grey: #d9dadc;
    --device-dark: #8a8c8f;
  }
  html, body {
    margin: 0;
    width: 1200px;
    height: 1200px;
    overflow: hidden;
    background: var(--stage);
  }
  .card {
    position: absolute;
    left: 193px;
    top: 30px;
    width: 814px;
    height: 1140px;
    background: var(--card);
    overflow: hidden;
  }
  .festive-pattern {
    position: absolute;
    inset: 0;
    background: radial-gradient(ellipse at center, var(--card) 35%, var(--doodle) 100%);
  }
  .brand {
    position: absolute;
    left: 330px;
    top: 92px;
    display: flex;
    align-items: center;
    gap: 14px;
    font-family: "Roboto", sans-serif;
    font-weight: 700;
    font-size: 36px;
    color: var(--brand-grey);
    white-space: nowrap;
  }
  .brand-mark {
    width: 32px;
    height: 32px;
    background: var(--brand-orange);
  }
  .greeting {
    position: absolute;
    left: 0;
    right: 0;
    margin: 0;
    text-align: center;
    font-family: "Yellowtail", cursive;
    font-weight: 400;
    color: var(--script-red);
    white-space: nowrap;
    line-height: 1;
    text-shadow:
      3px 3px 0 var(--card),
      10px 12px 0 var(--script-tan),
      14px 16px 0 var(--doodle);
  }
  .greeting-happy {
    top: 150px;
    font-size: 200px;
    transform: translateX(-20px) rotate(-4deg);
  }
  .greeting-newyear {
    top: 345px;
    font-size: 175px;
    transform: translateX(20px) rotate(-4deg);
  }
  .year {
    position: absolute;
    left: 0;
    right: 0;
    top: 592px;
    text-align: center;
    font-family: "Anton", sans-serif;
    font-size: 240px;
    line-height: 1;
    letter-spacing: 0;
  }
  .year-outline,
  .year-fill {
    position: absolute;
    left: 0;
    right: 0;
  }
  .year-outline {
    color: transparent;
    -webkit-text-stroke: 2px var(--year-red);
    transform: translate(-8px, -10px);
  }
  .year-fill {
    color: var(--year-red);
  }
  .device-photo {
    position: absolute;
    left: 322px;
    top: 790px;
    width: 180px;
    height: 285px;
    border-radius: 50px 50px 40px 40px;
    background: linear-gradient(180deg, var(--device-grey) 0%, #eeeeef 50%, var(--device-dark) 100%);
  }
  .website {
    position: absolute;
    left: 0;
    right: 0;
    top: 1080px;
    margin: 0;
    text-align: center;
    font-family: "Roboto", sans-serif;
    font-weight: 500;
    font-size: 26px;
    letter-spacing: 0.5px;
    color: var(--script-red);
  }
</style>
</head>
<body>
  <main class="card">
    <div class="festive-pattern" role="img" aria-label="Line-drawn pattern of party hats, champagne glasses, candles, pine cones, streamers, stars and fireworks"></div>

    <div class="brand">
      <span class="brand-mark"></span>
      <span class="brand-name">Corvane Medical</span>
    </div>

    <h1 class="greeting greeting-happy">Happy</h1>
    <p class="greeting greeting-newyear">New Year</p>

    <div class="year" aria-label="2022">
      <span class="year-outline" aria-hidden="true">2022</span>
      <span class="year-fill">2022</span>
    </div>

    <div class="device-photo" role="img" aria-label="Photo of the company's grey neck-worn medical device with its mouthpiece and cable"></div>

    <p class="website">www.corvanemedical.com</p>
  </main>
</body>
</html>
```